Landing Page Design für Tor- und Zaunbaufirma
Zielgruppe
der Kunde ist eine Tor- und Zaunbaufirma. Die Zielgruppen sind private Häuslebauer und Firmen.
Aufgabenstellung
Die Farben des Logos sollen nur sehr sparsam eingesetzt werden.
Die Navigation soll sich an der jetzigen Webseite orientieren. www.frenk-gitterwerk.de
Impressum und Datenschutz dezenter platzieren
Kommunikationsdaten vordergründig darstellen
mehr als 25-Jahre Erfahrung im Tor- und Zaunbau
Regionalität beachten

```html
<!DOCTYPE html>
<html lang="de">
<head>
<meta charset="utf-8">
<title>Tor &amp; Zaunbau Frenk</title>
<link rel="stylesheet" href="https://fonts.googleapis.com/css2?family=Nunito:ital,wght@0,800;0,900;1,700;1,800;1,900&display=swap">
<style>
  :root {
    --pink: #e8008e;
    --coral: #fb6b68;
    --blue: #2a8ee8;
    --sky: #38a8f0;
    --navy: #2c3590;
    --violet: #6c5ce6;
    --cyan: #2ec8dc;
    --arrow: #e33a3a;
    --white: #ffffff;
    --grey: #dcdcdc;
  }
  * { margin: 0; padding: 0; box-sizing: border-box; }
  html, body { width: 1200px; height: 675px; overflow: hidden; background: var(--white); }
  body { position: relative; font-family: "Nunito", sans-serif; font-style: italic; font-weight: 800; }
  .abs { position: absolute; }

  .brand { left: 129px; top: 22px; display: flex; align-items: center; gap: 8px;
    font-style: normal; font-weight: 900; font-size: 17px; color: var(--pink); white-space: nowrap; }
  .brand-dot { width: 14px; height: 14px; background: var(--pink); }

  .contact { left: 334px; top: 10px; color: var(--pink); font-size: 20px; line-height: 24px; font-weight: 900; }

  .privacy { left: 1027px; top: 2px; font-size: 9px; color: var(--sky); font-weight: 900; }
  .tagline { right: 117px; top: 29px; font-size: 17px; color: var(--sky); font-weight: 900; white-space: nowrap; }
  .tagline .years { font-size: 27px; }
  .tagline .strong { color: var(--blue); }

  .nav { left: 0; top: 87px; width: 1190px; height: 71px;
    background: linear-gradient(90deg, var(--pink) 0%, var(--pink) 38%, var(--coral) 62%, var(--coral) 100%); }
  .nav a { position: absolute; top: 24px; color: var(--white); text-decoration: none;
    font-size: 18px; font-weight: 900; white-space: nowrap; }

  .carousel { left: 0; top: 0; }
  .tile { position: absolute; top: 227px; width: 188px; height: 111px; }
  .tile-a { left: 282px; background: linear-gradient(180deg, #7a7c80 0%, #6d6f72 75%, #5b7a3a 100%); }
  .tile-b { left: 504px; background: linear-gradient(180deg, #3f6a2e 0%, #7b8f5a 40%, #b9682a 75%, #5b7a3a 100%); }
  .tile-c { left: 726px; background: linear-gradient(180deg, #2e4a2a 0%, #4a6a3a 45%, #3a3f3c 70%, #8a9088 100%); }
  .caption { position: absolute; top: 304px; width: 200px; text-align: center; color: var(--white);
    font-size: 17px; font-weight: 900; }

  .headline { left: 0; width: 1190px; top: 412px; text-align: center; color: var(--blue); font-size: 34px; font-weight: 900; }
  .subline { left: 0; width: 1190px; top: 466px; text-align: center; color: var(--blue); font-size: 24px; line-height: 29px; font-weight: 800; }
  .intro { left: 205px; width: 770px; top: 547px; text-align: center; color: var(--blue); font-size: 11px; line-height: 13px; font-weight: 700; }

  .chat { left: 13px; top: 536px; width: 39px; height: 39px; border-radius: 50%; background: var(--grey); }
</style>
</head>
<body>
  <div class="abs brand"><span class="brand-dot"></span>Tor &amp; Zaunbau Frenk</div>

  <div class="abs contact">
    0371 / 555 01 42<br>
    0172 / 555 83 19<br>
    info@frenk-gitterwerk.de
  </div>

  <div class="abs privacy">Datenschutz</div>
  <div class="abs tagline">Mehr als <span class="years">25</span> Jahre im <span class="strong">Tor- und Zaunbau!</span></div>

  <nav class="abs nav">
    <a href="#" style="left:333px">Über Uns</a>
    <a href="#" style="left:474px">Unsere Leistungen</a>
    <a href="#" style="left:705px">Kontakt</a>
    <a href="#" style="left:831px">Impressum</a>
  </nav>

  <svg class="abs carousel" width="1200" height="675" viewBox="0 0 1200 675">
    <defs>
      <linearGradient id="carousel-fill" x1="0" x2="1" y1="0" y2="0">
        <stop offset="0" stop-color="#2c3590"/>
        <stop offset="0.55" stop-color="#6c5ce6"/>
        <stop offset="0.8" stop-color="#6a6cec"/>
        <stop offset="1" stop-color="#2ec8dc"/>
      </linearGradient>
    </defs>
    <path d="M261 191 L934 191 Q1019 240 1019 282 Q1019 324 934 373 L261 373 Q178 324 178 282 Q178 240 261 191 Z" fill="url(#carousel-fill)"/>
    <polygon points="260,242 220,281 260,320" fill="var(--arrow)"/>
    <polygon points="936,242 976,281 936,320" fill="var(--arrow)"/>
  </svg>

  <div class="tile tile-a" role="img" aria-label="Foto einer grauen Sichtschutzanlage auf Rasen"></div>
  <div class="tile tile-b" role="img" aria-label="Foto eines Holzzauns vor einem Haus mit Garten"></div>
  <div class="tile tile-c" role="img" aria-label="Foto eines dunklen Metallzauns mit Tor"></div>
  <div class="caption" style="left:276px">Sichtschutzanlagen</div>
  <div class="caption" style="left:498px">Holzzäune</div>
  <div class="caption" style="left:720px">Metallzäune</div>

  <h1 class="abs headline">Tor &amp; Zaunbau Frenk aus Chemnitz</h1>
  <h2 class="abs subline">Ihr Partner für alle Zaun- und Torsysteme<br>in den Regionen Chemnitz und Zwickau.</h2>
  <p class="abs intro">Wenn es um Zäune, Toranlagen, Schranken geht, ob als Objektschutz für Industrieanlagen, als Lärmschutz für öffentliche Einrichtungen oder ganz einfach als Schmuck und Schutz vor Einblicken im Privatbereich – bei Tor &amp; Zaunbau Frenk können Sie sich auf einen Rund-Um-Service verlassen.</p>

  <div class="abs chat"></div>
</body>
</html>
```